Commercial Construction Company

We need a business card design based on our current logo. We are a commercial general contractor based in Southern California that specializes in bank remodels. We would like to see designs that incorporate dark blue. The final design should portray an image of professionalism and quality.

If possible, I would like to add metallic foil to the design. Thank you

```html
<!DOCTYPE html>
<html lang="en">
<head>
<meta charset="UTF-8">
<title>Northline Builders – Business Card</title>
<link href="https://fonts.googleapis.com/css2?family=Oswald:wght@400;500&family=Poppins:wght@400;600&display=swap" rel="stylesheet">
<style>
  :root {
    --backdrop: #5b636f;
    --card-white: #ffffff;
    --navy: #0b3c86;
    --navy-deep: #062b66;
    --navy-mid: #0a3a80;
    --emboss: #1c5cc0;
    --grey-text: #4a4a4a;
    --grey-title: #9a9a9a;
    --divider: #c9c9c9;
  }
  * { margin: 0; padding: 0; box-sizing: border-box; }
  html, body { width: 1200px; height: 800px; overflow: hidden; }
  body {
    background: var(--backdrop);
    display: flex;
    align-items: center;
    justify-content: center;
    gap: 40px;
  }
  .card {
    width: 540px;
    height: 309px;
    position: relative;
    box-shadow: 0 14px 30px rgba(0,0,0,0.35);
  }
  .card-front {
    background: var(--card-white);
    display: flex;
    align-items: center;
    padding-left: 100px;
  }
  .identity { text-align: right; padding-right: 18px; }
  .identity .name {
    font-family: "Oswald", sans-serif;
    font-weight: 500;
    font-size: 26px;
    letter-spacing: 0.5px;
    color: var(--navy);
    line-height: 1;
  }
  .identity .title {
    font-family: "Oswald", sans-serif;
    font-weight: 400;
    font-size: 15px;
    letter-spacing: 0.5px;
    color: var(--grey-title);
    margin-top: 4px;
  }
  .divider { width: 1px; height: 82px; background: var(--divider); }
  .contact {
    padding-left: 18px;
    font-family: "Poppins", sans-serif;
    font-size: 11.5px;
    color: var(--grey-text);
    line-height: 1.45;
  }
  .contact .address { margin-bottom: 4px; }
  .contact .row { display: flex; align-items: center; gap: 7px; }
  .contact svg { width: 10px; height: 10px; fill: var(--navy); flex: none; }
  .card-back {
    background: linear-gradient(135deg, var(--navy-deep) 0%, var(--navy-mid) 55%, var(--navy-deep) 100%);
    display: flex;
    align-items: center;
    justify-content: center;
    gap: 14px;
  }
  .brand-mark {
    width: 34px; height: 34px;
    border-radius: 50%;
    background: var(--emboss);
  }
  .brand-name {
    font-family: "Poppins", sans-serif;
    font-weight: 600;
    font-size: 34px;
    letter-spacing: 2px;
    color: var(--emboss);
  }
</style>
</head>
<body>
  <section class="card card-front">
    <div class="identity">
      <div class="name">DANIEL REYES</div>
      <div class="title">PRESIDENT</div>
    </div>
    <div class="divider"></div>
    <div class="contact">
      <div class="address">4120 Harbor Crest Way<br>Riverside, California 92501</div>
      <div class="row">
        <svg viewBox="0 0 24 24"><path d="M6.6 10.8a15.1 15.1 0 0 0 6.6 6.6l2.2-2.2a1 1 0 0 1 1-.25 11.4 11.4 0 0 0 3.6.57 1 1 0 0 1 1 1V20a1 1 0 0 1-1 1A17 17 0 0 1 3 4a1 1 0 0 1 1-1h3.5a1 1 0 0 1 1 1c0 1.25.2 2.45.57 3.57a1 1 0 0 1-.25 1z"/></svg>
        <span>951-555-0142</span>
      </div>
      <div class="row">
        <svg viewBox="0 0 24 24"><path d="M2 5h20v14H2z M2 5l10 8 10-8" /></svg>
        <span>hello@northline.com</span>
      </div>
      <div class="row">
        <svg viewBox="0 0 24 24"><circle cx="12" cy="12" r="10"/></svg>
        <span>www.northline.com</span>
      </div>
    </div>
  </section>

  <section class="card card-back">
    <div class="brand-mark"></div>
    <div class="brand-name">NORTHLINE</div>
  </section>
</body>
</html>
```